Maple Row Yardcare

I want it as prefession and attractive as possible we are a lawnmowing business

Phone number 605-318-2264
Name- Carl Whitby
Email- mapleroweyardsd@fernpost.net

```html
<!DOCTYPE html>
<html lang="en">
<head>
<meta charset="utf-8">
<title>Maple Row Yardcare – Business Card</title>
<link rel="stylesheet" href="https://fonts.googleapis.com/css2?family=Oswald:wght@600&family=Roboto:wght@400;500&family=Montserrat:wght@500&display=swap">
<style>
  :root {
    --backdrop: #262626;
    --forest: #0a5a34;
    --forest-deep: #074a2b;
    --forest-soft: #1a6e42;
    --leaf: #4ea23a;
    --ink: #0b4d2b;
    --paper: #f1f1f0;
    --paper-shade: #e6e6e5;
    --mist: #d7e8dc;
  }
  * { margin: 0; padding: 0; box-sizing: border-box; }
  html, body { width: 1200px; height: 576px; overflow: hidden; background: var(--backdrop); }
  .stage { position: relative; width: 1200px; height: 576px; }

  .card { position: absolute; top: 138px; height: 292px; border-radius: 10px; overflow: hidden; box-shadow: 0 4px 10px rgba(0,0,0,0.45); }

  /* Front */
  .card-front { left: 102px; width: 484px; background: linear-gradient(160deg, var(--forest) 0%, var(--forest-deep) 100%); }
  .front-decoration {
    position: absolute; left: 0; top: 0; width: 230px; height: 292px;
    background: linear-gradient(90deg, rgba(255,255,255,0.05), rgba(255,255,255,0));
  }
  .front-wordmark {
    position: absolute; left: 0; right: 0; top: 124px; text-align: center;
    font-family: "Oswald", sans-serif; font-weight: 600; font-size: 32px;
    letter-spacing: 1px; text-transform: uppercase; color: var(--forest-soft);
  }
  .front-url {
    position: absolute; left: 0; right: 0; top: 262px; text-align: center;
    font-family: "Montserrat", sans-serif; font-weight: 500; font-size: 13px;
    letter-spacing: 3px; color: var(--mist);
  }

  /* Back */
  .card-back { left: 596px; width: 480px; background: linear-gradient(180deg, var(--paper) 0%, var(--paper-shade) 100%); }
  .back-wordmark {
    position: absolute; left: 41px; top: 34px; display: flex; align-items: center; gap: 8px;
    font-family: "Oswald", sans-serif; font-weight: 600; font-size: 20px; line-height: 1.05;
    text-transform: uppercase; color: var(--ink); letter-spacing: 0.5px;
  }
  .back-wordmark .mark-square { width: 16px; height: 16px; background: var(--leaf); flex: none; }
  .holder { position: absolute; left: 264px; top: 64px; }
  .holder-name {
    font-family: "Oswald", sans-serif; font-weight: 600; font-size: 23px;
    text-transform: uppercase; letter-spacing: 0.5px; color: var(--ink); line-height: 1.2;
  }
  .holder-name .surname { color: var(--leaf); }
  .holder-company { font-family: "Roboto", sans-serif; font-size: 13px; color: var(--ink); margin-top: 1px; }
  .contact-list { position: absolute; left: 266px; top: 124px; list-style: none; }
  .contact-list li {
    display: flex; align-items: center; gap: 11px; height: 18px;
    font-family: "Roboto", sans-serif; font-size: 12.5px; color: var(--ink);
  }
  .contact-list svg { width: 12px; height: 12px; fill: var(--leaf); flex: none; }
  .mowing-scene {
    position: absolute; left: 0; top: 136px; width: 244px; height: 156px;
    background: linear-gradient(135deg, var(--forest-soft) 0%, var(--forest-deep) 100%);
    border-top-right-radius: 10px;
  }
  .follow-band {
    position: absolute; left: 254px; bottom: 0; width: 226px; height: 35px;
    background: var(--leaf);
    border-top-left-radius: 16px;
    display: flex; align-items: center; justify-content: center; padding-left: 12px;
    font-family: "Roboto", sans-serif; font-size: 12.5px; color: var(--ink);
  }
</style>
</head>
<body>
<main class="stage">
  <section class="card card-front" aria-label="Card front">
    <div class="front-decoration" role="img" aria-label="Faint silhouette of a worker pushing a lawn mower"></div>
    <p class="front-wordmark">Maple Row Yardcare</p>
    <p class="front-url">www.maplerowyardcare.com</p>
  </section>

  <section class="card card-back" aria-label="Card back">
    <div class="back-wordmark"><span class="mark-square"></span><span>Maple Row<br>Yardcare</span></div>
    <div class="holder">
      <p class="holder-name">Carl <span class="surname">Whitby</span></p>
      <p class="holder-company">Maple Row Yardcare</p>
    </div>
    <ul class="contact-list">
      <li>
        <svg viewBox="0 0 24 24" aria-hidden="true"><path d="M6.6 10.8a15 15 0 0 0 6.6 6.6l2.2-2.2a1 1 0 0 1 1-.25 11.4 11.4 0 0 0 3.6.57 1 1 0 0 1 1 1V20a1 1 0 0 1-1 1A17 17 0 0 1 3 4a1 1 0 0 1 1-1h3.5a1 1 0 0 1 1 1c0 1.25.2 2.45.57 3.6a1 1 0 0 1-.25 1z"/></svg>
        605-318-2264
      </li>
      <li>
        <svg viewBox="0 0 24 24" aria-hidden="true"><path d="M2 5h20v2l-10 7L2 7z M2 8.5l7 5.2-7 4.8z M22 8.5v10l-7-4.8z M10.4 14.6 12 15.8l1.6-1.2 7.4 4.4H3z"/></svg>
        mapleroweyardsd@fernpost.net
      </li>
    </ul>
    <div class="mowing-scene" role="img" aria-label="Silhouette of a worker mowing grass with a push mower"></div>
    <div class="follow-band">Follow us on: /maplerowyardcare</div>
  </section>
</main>
</body>
</html>
```